Create for us a Shop-Stopper Business Card

We need a standout, first class business card to go along with our new brand strategy. Sleek, Contemporary and fresh.

Colors and theme must sync with our websitewww.pelvorpower.co.uk

We want a business card that has a global brand appeal. TKR Energy is a small UK renewable company that specialises in energy projects in Africa. We want a business card that has the following characteristics: Very short, precise, global, stand out, NOT TOO LOUD but contemporary. The company's colour themes are White, Grey with a hint of green.

Target Market(s)

Business exec, high net worth individuals, investors, commercial leaders, suppliers, government officials

Industry/Entity Type

Solar Energy

Contact Information for Business Card

Logo, Name, Title, Address, web address, email,

Requirements
Must have
• Logo must be sharp
Nice to have
• Adapt fonts from the logo. The large circular side of the logo at the back in a very refreshing way
Should not have
• No solar panel shapes or image.Very little black. If possible avoid black. Its not coming out nice. I think !!!

```html
<!DOCTYPE html>
<html lang="en">
<head>
<meta charset="utf-8">
<title>TKR Energy – Business Card</title>
<link rel="stylesheet" href="https://fonts.googleapis.com/css2?family=Roboto:wght@400;500;700&display=swap">
<style>
  :root {
    --backdrop: #5cc8ec;
    --green-light: #7fae42;
    --green-bright: #1fbf5c;
    --green-deep: #3f7f22;
    --green-mid: #23a04a;
    --card-white: #ffffff;
    --ink-grey: #7d7d7d;
    --ink-soft: #9a9a9a;
  }
  * { box-sizing: border-box; margin: 0; padding: 0; }
  html, body {
    width: 1200px;
    height: 1200px;
    overflow: hidden;
    background: var(--backdrop);
    font-family: "Roboto", Arial, sans-serif;
  }
  .card-set {
    position: absolute;
    top: 340px;
    left: 50px;
    display: flex;
    gap: 60px;
  }
  .card {
    width: 520px;
    height: 520px;
    position: relative;
    box-shadow: 0 6px 18px rgba(0, 60, 90, 0.18);
  }
  /* front */
  .card-front {
    background:
      linear-gradient(200deg, rgba(31,191,92,0.9) 0%, rgba(31,191,92,0) 55%),
      linear-gradient(160deg, var(--green-light) 0%, var(--green-deep) 100%);
  }
  .brand {
    position: absolute;
    left: 48px;
    bottom: 70px;
    display: flex;
    align-items: center;
    gap: 16px;
    color: var(--card-white);
  }
  .brand-dot {
    width: 58px;
    height: 58px;
    border: 5px solid var(--card-white);
    border-radius: 50%;
  }
  .brand-name {
    font-size: 38px;
    font-weight: 500;
    letter-spacing: 2px;
  }
  /* back */
  .card-back { background: var(--card-white); color: var(--ink-grey); }
  .holder {
    position: absolute;
    left: 100px;
    top: 210px;
  }
  .holder-name {
    font-size: 40px;
    font-weight: 700;
    line-height: 1.1;
  }
  .holder-line {
    font-size: 21px;
    color: var(--ink-soft);
    line-height: 1.35;
  }
  .holder-line.email { margin-top: 4px; }
  .company {
    position: absolute;
    left: 150px;
    top: 390px;
    display: flex;
    align-items: center;
    gap: 48px;
  }
  .company-dot {
    width: 54px;
    height: 54px;
    border: 5px solid var(--ink-soft);
    border-radius: 50%;
  }
  .company-web {
    font-size: 16px;
    font-weight: 700;
    color: var(--ink-grey);
  }
  .company-address {
    font-size: 15px;
    color: var(--ink-soft);
    line-height: 1.3;
  }
</style>
</head>
<body>
  <main class="card-set">
    <section class="card card-front" aria-label="Card front">
      <div class="brand">
        <span class="brand-dot"></span>
        <span class="brand-name">TKR ENERGY</span>
      </div>
    </section>

    <section class="card card-back" aria-label="Card back">
      <div class="holder">
        <p class="holder-name">Name Lastname</p>
        <p class="holder-line email">email@pelvorpower.co.uk</p>
        <p class="holder-line">TKR:CEO</p>
      </div>
      <div class="company">
        <span class="company-dot"></span>
        <div class="company-details">
          <p class="company-web">www.pelvorpower.co.uk</p>
          <p class="company-address">58 Harbour Lane, East Marsh<br>E9 4QT | London</p>
        </div>
      </div>
    </section>
  </main>
</body>
</html>
```